Let Us Bloom speaking engagement

the flyer is about a speaking engagement for women's groups. Flyer should be simple, soft, engaging, clean and professional. I am a life coach and also a talk show host. the event I will be advertising is for groups of women. It will be given to church groups, female clubs and organizations. The name of my company is Mara's Lantern Life Coaching Institute.

Target Market(s)

professional women over thirty years old

Font styles to use
Script

Colors
ffffff
34a7d8
85cae6

Requirements
Must have
• use my photo and logo only
Should not have
• anything distracting

```html
<!DOCTYPE html>
<html lang="en">
<head>
<meta charset="utf-8">
<title>Let Us Bloom – Speaking Engagement Flyer</title>
<link rel="stylesheet" href="https://fonts.googleapis.com/css2?family=Josefin+Sans:wght@600&family=Great+Vibes&family=Fira+Sans:ital,wght@0,400;1,600&family=Marcellus&display=swap">
<style>
  :root {
    --white: #ffffff;
    --brand-blue: #34a7d8;
    --soft-blue: #85cae6;
    --pale-blue: #d6eef8;
    --ink: #1b2a33;
    --text: #222a30;
    --muted-grey: #8f9aa2;
    --heart: #34a7d8;
  }
  * { margin: 0; padding: 0; box-sizing: border-box; }
  html, body { width: 800px; height: 1200px; overflow: hidden; background: var(--white); }
  .flyer { position: relative; width: 800px; height: 1200px; background: var(--white); }

  .hero {
    position: absolute; left: 0; top: 0; width: 800px; height: 475px;
    background:
      radial-gradient(ellipse 240px 190px at 560px 250px, var(--white) 0%, rgba(255,255,255,0.8) 35%, rgba(255,255,255,0) 100%),
      linear-gradient(180deg, var(--brand-blue) 0%, var(--soft-blue) 38%, var(--pale-blue) 70%, var(--white) 100%);
  }
  .hero-title {
    position: absolute; right: 44px; top: 152px; text-align: right;
    font-family: "Josefin Sans", sans-serif; font-weight: 600; color: var(--ink);
    font-size: 40px; line-height: 44px;
  }
  .hero-title .heart { display: inline-block; width: 22px; height: 20px; vertical-align: 2px; }
  .hero-title .coach {
    display: block; margin-top: 6px;
    font-family: "Great Vibes", cursive; font-weight: 400; font-size: 48px; line-height: 52px;
  }

  .intro { position: absolute; left: 60px; top: 488px; width: 340px; }
  .intro-heading {
    font-family: "Fira Sans", sans-serif; font-style: italic; font-weight: 600;
    color: var(--brand-blue); font-size: 46px; line-height: 52px;
  }
  .intro-body {
    font-family: "Fira Sans", sans-serif; color: var(--text);
    font-size: 25px; line-height: 34px; margin-top: 4px;
  }

  .portrait {
    position: absolute; left: 470px; top: 510px; width: 280px; height: 210px;
    display: flex; align-items: center; justify-content: center;
    font-family: "Fira Sans", sans-serif; font-size: 21px; color: var(--muted-grey);
  }

  .invite-band {
    position: absolute; left: 0; top: 775px; width: 800px; height: 268px;
    background: var(--brand-blue);
  }
  .invite-frame {
    position: absolute; left: 46px; top: 22px; right: 46px; bottom: 22px;
    border: 2px solid var(--white); text-align: center; color: var(--white);
    font-family: "Marcellus", serif;
    display: flex; flex-direction: column; justify-content: center;
  }
  .invite-text { font-size: 29px; line-height: 34px; }
  .contact-label { font-size: 29px; line-height: 34px; margin-top: 34px; }
  .contact-phones { font-size: 42px; line-height: 46px; }
  .contact-phones .or { font-size: 33px; }

  .brand {
    position: absolute; left: 0; top: 1090px; width: 800px; text-align: center;
    font-family: "Marcellus", serif; font-size: 30px; color: var(--muted-grey);
  }
</style>
</head>
<body>
<main class="flyer">
  <section class="hero" role="img" aria-label="Photo: silhouette of a woman with open arms on a beach at sunrise under a soft blue sky">
    <h1 class="hero-title">
      A heart t<svg class="heart" viewBox="0 0 24 22" aria-hidden="true"><path d="M12 21 C4 14 0 10 0 6 A6 6 0 0 1 12 4 A6 6 0 0 1 24 6 C24 10 20 14 12 21Z" fill="var(--heart)"/></svg> heart<br>
      conversation with
      <span class="coach">Life Coach Lena Whitfield</span>
    </h1>
  </section>

  <section class="intro">
    <h2 class="intro-heading">Let Us Bloom</h2>
    <p class="intro-body">is an interactive soul searching session that will help women share their stories and be real about the things that matter most.</p>
  </section>

  <div class="portrait" role="img" aria-label="Portrait photo of the life coach">photo</div>

  <section class="invite-band">
    <div class="invite-frame">
      <p class="invite-text">To invite Lena to your women's<br>group or gathering.</p>
      <p class="contact-label">Contact us at</p>
      <p class="contact-phones">242-555-0148 <span class="or">or</span> 555-0192</p>
    </div>
  </section>

  <footer class="brand">Mara's Lantern Life Coaching Institute</footer>
</main>
</body>
</html>
```